Flyer für Immobilienmakler
Top Arbeit vom Designer. Er hat alle Idee schnell und professionell umgesetzt und das Ergebnis kann sich sehen lassen. Herzlichen Dank für die großartige Arbeit. Immer wieder gerne.
Zielgruppe
Immobilienmakler, Zielgruppe sind Menschen die uns weiterempfehlen um ihre Immobilie zu verkaufen
Aufgabenstellung
Ein Flyer DIN lang quer, Vorder und Rückseite, Es geht um eine Tippgeberprovision welche Menschen bekommen die uns einen Verkaufskunden bringen, diese erhalten 10 %- genaue Texte und Hinweise werde ich einbringen, Unser Slogan: 'Unsere Erfahrung für Ihren Vorteil'
Nachtrag. Bei dem Flyer 'Vom Berg Immobilien' finde ich die blauen Banner/ Streifen gut- ist aber kein Muss. Update: Es war als Inspiration von meiner Seite gedacht. Auf keinen Fall darf es genauso aussehen!!
Meine jetzige Webseite ist auch gut um die Farben zu erkennen, jedoch nicht unbedingt das Design, da ich gerade eine neue Webseite erstellen lasse

```html
<!DOCTYPE html>
<html lang="de">
<head>
<meta charset="utf-8">
<title>Tippgeber-Flyer – Lindqvarth Immobilien</title>
<link rel="stylesheet" href="https://fonts.googleapis.com/css2?family=Montserrat:wght@400;500;600&display=swap">
<style>
  :root {
    --page-bg: #ffffff;
    --board-bg: #f6f6f6;
    --navy: #2b2d5e;
    --white: #ffffff;
    --photo-dark: #2c3d40;
    --photo-mid: #4b5c5e;
    --caption: #8a8a8a;
  }
  * { margin: 0; padding: 0; box-sizing: border-box; }
  html, body {
    width: 1200px; height: 1200px; overflow: hidden;
    background: var(--page-bg);
    font-family: "Montserrat", sans-serif;
  }
  .board {
    position: absolute; left: 81px; top: 81px;
    width: 1037px; height: 1037px;
    background: var(--board-bg);
  }
  .flyer {
    position: absolute; left: 153px; top: 376px;
    width: 893px; height: 447px;
    overflow: hidden;
    box-shadow: 0 3px 8px rgba(0,0,0,0.18);
  }
  .flyer-photo {
    position: absolute; inset: 0;
    background:
      radial-gradient(ellipse 45% 40% at 55% 62%, rgba(160,130,110,0.55), transparent 70%),
      radial-gradient(ellipse 60% 50% at 50% 45%, var(--photo-mid), transparent 75%),
      linear-gradient(180deg, var(--photo-dark) 0%, #3c4c4f 55%, #2a3739 100%);
  }
  .commission-badge {
    position: absolute; left: 22px; top: 22px;
    width: 135px; height: 135px;
  }
  .slogan {
    position: absolute; left: 23px; top: 362px;
    color: var(--white);
    font-size: 31px; font-weight: 500;
    line-height: 40px; letter-spacing: 0.115em;
    text-transform: uppercase;
    white-space: nowrap;
  }
  .brand-tab {
    position: absolute; left: 609px; top: 0;
    width: 263px; height: 88px;
    background: var(--white);
    border-radius: 0 0 16px 16px;
    display: flex; align-items: center; justify-content: center;
  }
  .brand-name {
    color: var(--navy);
    font-size: 19px; font-weight: 600;
    letter-spacing: 0.01em;
    white-space: nowrap;
  }
  .web-tab {
    position: absolute; left: 609px; top: 394px;
    width: 263px; height: 53px;
    background: var(--white);
    border-radius: 16px 16px 0 0;
    display: flex; align-items: center; justify-content: center;
  }
  .web-address {
    color: var(--navy);
    font-size: 16px; font-weight: 400;
    letter-spacing: 0.04em;
    white-space: nowrap;
  }
  .caption {
    position: absolute; left: 262px; top: 984px;
    width: 676px;
    text-align: center;
    color: var(--caption);
    font-size: 12.5px; line-height: 21px;
  }
</style>
</head>
<body>
  <div class="board"></div>

  <section class="flyer">
    <div class="flyer-photo" role="img" aria-label="Foto: wachsende Münzstapel mit kleinen weißen Häusern darauf vor dunklem Hintergrund mit angedeutetem Balkendiagramm"></div>

    <svg class="commission-badge" viewBox="0 0 135 135" aria-label="10 Prozent Tippgeberprovision">
      <defs>
        <path id="badge-ring" d="M67.5,67.5 m-55,0 a55,55 0 1,1 110,0 a55,55 0 1,1 -110,0"/>
      </defs>
      <circle cx="67.5" cy="67.5" r="67" fill="#ffffff"/>
      <circle cx="67.5" cy="67.5" r="46" fill="none" stroke="#2b2d5e" stroke-width="1" stroke-dasharray="1 2.2"/>
      <text font-family="Montserrat, sans-serif" font-size="10" font-weight="500" fill="#2b2d5e" letter-spacing="1.6">
        <textPath href="#badge-ring" startOffset="0">TIPPGEBERPROVISION · TIPPGEBERPROVISION ·</textPath>
      </text>
      <g transform="rotate(-25 67.5 67.5)">
        <text x="67.5" y="69" text-anchor="middle" font-family="Montserrat, sans-serif" font-size="34" font-weight="600" fill="#2b2d5e">10</text>
        <text x="67.5" y="86" text-anchor="middle" font-family="Montserrat, sans-serif" font-size="9.5" fill="#2b2d5e" letter-spacing="1.5">PROZENT</text>
      </g>
    </svg>

    <h1 class="slogan">Unsere Erfahrung für<br>Ihren Vorteil</h1>

    <div class="brand-tab">
      <span class="brand-name">Lindqvarth Immobilien</span>
    </div>

    <div class="web-tab">
      <span class="web-address">www.lindqvarth-immo.de</span>
    </div>
  </section>

  <p class="caption">Lorem ipsum dolor sit amet, consetetur sadipscing elitr, sed diam nonumy eirmod tempor invidunt ut labore et dolore magna aliquyam erat, sed diam voluptua. At vero eos et accusam et justo duo dolores et ea rebum. Stet clita kasd gubergren, no sea takimata sanctus est.</p>
</body>
</html>
```